Talvena Brooke R&B Mixtape CD Cover

We need a cd cover for an r&b mixtape. The artist's name is Talvena Brooke and the name of the mixtape is 4:17. The cover should reflect a vibe of 4:17 am in the morning where a young female has concluded clubbing and the night is left open ended, meaning it could be the beginning of a whole new morning or the night not ending. The cover should be creative and reflect the essence of a breakout artist. The cover will be used as the visual for all online music posts i.e. mixvault, tunelodge, echoharbor, etc. Artist name and the title of the mixtape should be included on the cover.

Target Market(s)

R&B music lovers aged 19-39.

Industry/Entity Type

Music Download

Requirements
Must have
• Reflecting of time and having a good time.

```html
<!DOCTYPE html>
<html lang="en">
<head>
<meta charset="utf-8">
<title>Talvena Brooke – 4:17</title>
<link rel="stylesheet" href="https://fonts.googleapis.com/css2?family=Michroma&family=Orbitron:wght@500&display=swap">
<style>
  :root {
    --violet: #5b4a9a;
    --violet-deep: #3a3478;
    --indigo: #4a5fb0;
    --amber: #d89a3a;
    --rose: #c85a7a;
    --ember: #b8452e;
    --frame: #5a3a22;
    --silver: #eceef3;
    --silver-shade: #6b6a78;
    --white: #ffffff;
  }
  html, body {
    margin: 0;
    padding: 0;
    width: 1200px;
    height: 1200px;
    overflow: hidden;
    background: var(--violet-deep);
  }
  .cover {
    position: relative;
    width: 1200px;
    height: 1200px;
    overflow: hidden;
  }
  .collage-backdrop {
    position: absolute;
    inset: 0;
    background:
      radial-gradient(circle at 20% 25%, rgba(216,154,58,.55), transparent 32%),
      radial-gradient(circle at 85% 15%, rgba(90,170,200,.45), transparent 30%),
      radial-gradient(circle at 12% 85%, rgba(200,90,122,.7), transparent 35%),
      radial-gradient(circle at 90% 70%, rgba(220,220,240,.35), transparent 28%),
      radial-gradient(circle at 55% 95%, rgba(216,154,58,.45), transparent 30%),
      linear-gradient(160deg, var(--violet) 0%, var(--indigo) 45%, var(--violet-deep) 100%);
  }
  .frame {
    position: absolute;
    border: 34px solid var(--frame);
    opacity: .55;
  }
  .frame--left { left: -40px; top: 100px; width: 380px; height: 400px; }
  .frame--right { left: 520px; top: 240px; width: 570px; height: 480px; }
  .frame--bottom { left: -20px; top: 840px; width: 600px; height: 420px; border-color: var(--ember); opacity: .45; }
  .clock-art {
    position: absolute;
    left: -40px; top: 180px;
    width: 330px; height: 330px;
    border-radius: 50%;
    background: radial-gradient(circle, rgba(240,210,150,.45), rgba(150,110,170,.25) 70%, transparent 72%);
  }
  .chandelier-art {
    position: absolute;
    left: 290px; top: 0;
    width: 620px; height: 740px;
    background: radial-gradient(ellipse at 50% 45%, rgba(230,200,150,.75), rgba(200,160,110,.35) 55%, transparent 75%);
  }
  .lightning-art {
    position: absolute;
    left: 760px; top: 290px;
    width: 290px; height: 400px;
    background: radial-gradient(ellipse at 55% 50%, rgba(220,225,255,.5), rgba(150,160,230,.2) 55%, transparent 75%);
  }
  .artist-name {
    position: absolute;
    left: 0; right: 0; top: 630px;
    margin: 0;
    text-align: center;
    font-family: "Michroma", sans-serif;
    font-weight: 400;
    font-size: 74px;
    line-height: 96px;
    color: var(--silver);
    text-shadow: 2px 3px 3px var(--silver-shade), 0 0 2px #ffffff;
  }
  .artist-name span { display: block; }
  .mixtape-title {
    position: absolute;
    left: 0; right: 0; top: 820px;
    margin: 0;
    text-align: center;
    font-family: "Orbitron", sans-serif;
    font-weight: 500;
    font-size: 350px;
    line-height: 330px;
    letter-spacing: 20px;
    color: var(--white);
    text-shadow: 3px 5px 6px rgba(60,50,90,.6), 0 0 3px rgba(255,255,255,.9);
  }
</style>
</head>
<body>
  <main class="cover">
    <div class="collage-backdrop" role="img" aria-label="Collage of purple damask wallpaper, night clouds and glowing coloured bokeh lights"></div>
    <div class="frame frame--left"></div>
    <div class="frame frame--right"></div>
    <div class="frame frame--bottom"></div>
    <div class="clock-art" role="img" aria-label="Faint clock face showing the early morning hour"></div>
    <div class="chandelier-art" role="img" aria-label="Lit crystal chandelier hanging from the top"></div>
    <div class="lightning-art" role="img" aria-label="Lightning bolt striking through storm clouds"></div>
    <h1 class="artist-name"><span>TALVENA</span><span>BROOKE</span></h1>
    <p class="mixtape-title">4:17</p>
  </main>
</body>
</html>
```